Velmora - 3D medical animations and high end visual content

Our company creates high end visual content and animations for medical global companies.
Our website - www.velmora-studio.example
We would like to have an amazing business card for our CEO that he can use in the following exhebitions he is going to attend.
It is very important that the design will be memorable and diffrent. It has to reflect our brand design (you can have it from our website)
We would like to transmit innovation, prestige, luxury, aesthetics.
The card has to be Double Sided

Target Market(s)

Marketing managers in medical global companys

Industry/Entity Type

It Company

Contact Information for Business Card

Requirements
Nice to have
• It is very important that the design will be memorable and diffrent. It has to reflect our brand design (you can have it from our website)

```html
<!DOCTYPE html>
<html lang="en">
<head>
<meta charset="utf-8">
<title>Velmora — Business Card</title>
<link rel="stylesheet" href="https://fonts.googleapis.com/css2?family=Montserrat:wght@400;500;600&family=Open+Sans:wght@400;600&display=swap">
<style>
  :root {
    --slate: #3f4350;
    --paper: #ffffff;
    --accent: #1a9ad6;
    --ink: #3a3d44;
    --backdrop: #eceef1;
    --shadow: rgba(30, 34, 44, 0.18);
  }
  * { box-sizing: border-box; margin: 0; padding: 0; }
  html, body {
    width: 1200px; height: 1200px; overflow: hidden;
    background: var(--backdrop);
    font-family: "Open Sans", Arial, sans-serif;
  }
  .sheet {
    width: 1200px; height: 1200px;
    display: flex; flex-direction: column; align-items: center; justify-content: center;
    gap: 70px;
  }
  .card {
    position: relative;
    width: 780px; height: 460px;
    background: var(--paper);
    box-shadow: 0 10px 30px var(--shadow);
    overflow: hidden;
  }
  /* Front */
  .card-front .field {
    position: absolute; left: 0; top: 0; width: 100%; height: 348px;
    background: var(--slate);
    display: flex; align-items: center; justify-content: center;
  }
  .wordmark {
    font-family: "Montserrat", Arial, sans-serif;
    font-weight: 500;
    font-size: 64px;
    letter-spacing: 3px;
    color: var(--paper);
  }
  .card-front .web {
    position: absolute; left: 0; bottom: 0; width: 100%; height: 112px;
    display: flex; align-items: center; justify-content: center; gap: 12px;
    font-size: 21px; color: var(--ink);
  }
  /* Back */
  .card-back .identity {
    position: absolute; left: 0; top: 150px; width: 100%;
    display: flex; justify-content: center; align-items: center;
  }
  .person { text-align: right; padding-right: 22px; border-right: 2px solid var(--ink); padding-top: 2px; padding-bottom: 2px; }
  .person-name {
    font-family: "Open Sans", Arial, sans-serif;
    font-size: 24px; letter-spacing: 1.5px; color: var(--accent); font-weight: 400;
    text-transform: uppercase;
  }
  .person-name .given { font-weight: 600; }
  .person-role { font-size: 17px; color: var(--ink); margin-top: 6px; }
  .phones { padding-left: 22px; display: flex; flex-direction: column; gap: 10px; }
  .phone-line { display: flex; align-items: center; gap: 10px; font-size: 21px; color: var(--ink); }
  .card-back .footer {
    position: absolute; left: 0; bottom: 0; width: 100%; height: 86px;
    background: var(--slate);
    display: flex; align-items: center; justify-content: center; gap: 12px;
    font-size: 20px; color: var(--paper);
  }
  .icon { width: 26px; height: 26px; flex: none; }
</style>
</head>
<body>
<main class="sheet">
  <section class="card card-front" aria-label="Card front">
    <div class="field">
      <span class="wordmark">VELMORA</span>
    </div>
    <div class="web">
      <svg class="icon" viewBox="0 0 26 26" aria-hidden="true">
        <circle cx="13" cy="13" r="12" fill="none" stroke="var(--accent)" stroke-width="1.6"/>
        <circle cx="13" cy="13" r="7" fill="none" stroke="var(--accent)" stroke-width="1.4"/>
        <ellipse cx="13" cy="13" rx="3" ry="7" fill="none" stroke="var(--accent)" stroke-width="1.2"/>
        <line x1="6" y1="13" x2="20" y2="13" stroke="var(--accent)" stroke-width="1.2"/>
      </svg>
      <span>www.velmora-studio.example</span>
    </div>
  </section>

  <section class="card card-back" aria-label="Card back">
    <div class="identity">
      <div class="person">
        <div class="person-name"><span class="given">Tavi</span> Orenstein</div>
        <div class="person-role">Founder &amp; CEO</div>
      </div>
      <div class="phones">
        <div class="phone-line">
          <svg class="icon" viewBox="0 0 26 26" aria-hidden="true">
            <circle cx="13" cy="13" r="12" fill="none" stroke="var(--accent)" stroke-width="1.6"/>
            <rect x="9" y="6" width="8" height="14" rx="1.5" fill="none" stroke="var(--accent)" stroke-width="1.5"/>
            <line x1="12" y1="17.5" x2="14" y2="17.5" stroke="var(--accent)" stroke-width="1.4"/>
          </svg>
          <span>+972-55-0142387</span>
        </div>
        <div class="phone-line">
          <svg class="icon" viewBox="0 0 26 26" aria-hidden="true">
            <circle cx="13" cy="13" r="12" fill="none" stroke="var(--accent)" stroke-width="1.6"/>
            <path d="M6 13.5 L13 7 L20 13.5 H18 V19 H15 V15.5 H11 V19 H8 V13.5 Z" fill="var(--accent)"/>
          </svg>
          <span>+972-73-0265914</span>
        </div>
      </div>
    </div>
    <div class="footer">
      <svg class="icon" viewBox="0 0 26 26" aria-hidden="true">
        <circle cx="13" cy="13" r="12" fill="none" stroke="var(--accent)" stroke-width="1.6"/>
        <rect x="6.5" y="8.5" width="13" height="9" fill="none" stroke="var(--accent)" stroke-width="1.4"/>
        <path d="M6.5 8.5 L13 14 L19.5 8.5" fill="none" stroke="var(--accent)" stroke-width="1.4"/>
      </svg>
      <span>tavi@velmora-studio.example</span>
    </div>
  </section>
</main>
</body>
</html>
```